Melbourne Locksmith Needs a Web Site

We need a web site for our new Locksmith business in Melbourne Australia. Our business is called " Calloway Lane Locksmiths" . (Calloway lane is a well known in the city and has the famous railway station , it is a main icon of melbourne . Maybe we could incorperate the station maybe in the front page or heading background. our services include Automotive Locksmithing ( Cuting keys to cars, opening cars etc / Master Keys Systems/ Commercial work / Domestic . Also we have no logo yet. but we can get that in the future if needed.

Target Market(s)

(Automotive ) Lost keys to cars, Trucks, Jammed Ignitions, Opening Vehicles. mobile locksmith in a van, Locked out of your house ?

Industry/Entity Type

Business

Number of Pages Required

4 page

Font styles to use
Sans Serif

Colors

Designer to choose colors to be used in the design.

Requirements
Must have
• Phone number easy to read on web site.
Nice to have
• map of where we are, show case pictures of common lock problems for automotive eg ( damaged keys/ Broken).

```html
<!DOCTYPE html>
<html lang="en">
<head>
<meta charset="utf-8">
<title>Calloway Lane Locksmiths</title>
<link rel="stylesheet" href="https://fonts.googleapis.com/css2?family=Lato:wght@400;700;900&family=Open+Sans:wght@400;600;700&display=swap">
<style>
:root{
  --green:#7dad48;
  --green-dark:#6a9a37;
  --ink:#1d1d1d;
  --text:#333;
  --muted:#9a9a9a;
  --light:#f4f5f6;
  --footer:#222222;
  --footer-base:#151515;
  --white:#fff;
}
*{margin:0;padding:0;box-sizing:border-box}
html,body{width:1200px;height:3291px;overflow:hidden}
body{font-family:"Open Sans",Arial,sans-serif;color:var(--text);background:var(--white);position:relative}
.abs{position:absolute}

/* top bar */
.topbar{left:0;top:0;width:1200px;height:22px;background:var(--ink);color:#ddd;font-size:9px}
.topbar span{position:absolute;display:flex;align-items:center;gap:5px;top:5px;white-space:nowrap}
.topbar svg{width:9px;height:9px;fill:#ddd}

/* hero */
.hero-panel{left:0;top:22px;width:458px;height:553px;background:var(--green)}
.hero-photo{left:458px;top:22px;width:742px;height:553px;background:radial-gradient(ellipse at 45% 45%,#6b6b6b 0%,#2e2e2e 45%,#0e0e0e 100%)}
.logo{left:186px;top:58px;color:var(--white);font-family:"Lato",sans-serif;font-weight:900;font-size:19px;line-height:20px;display:flex;align-items:center;gap:10px;text-transform:uppercase}
.logo i{width:14px;height:14px;background:var(--white);display:block}
.nav{top:58px;left:0;width:1200px;height:20px}
.nav a{position:absolute;color:var(--white);font-family:"Lato",sans-serif;font-weight:700;font-size:11px;text-decoration:none;letter-spacing:.5px;top:3px;white-space:nowrap}
.btn{position:absolute;display:flex;align-items:center;justify-content:center;font-family:"Lato",sans-serif;font-weight:700;font-size:11px;letter-spacing:.5px;text-transform:uppercase;border-radius:20px;color:var(--white);white-space:nowrap}
.btn-green{background:var(--green)}
.btn-dark{background:var(--ink)}
.hero-kicker{left:204px;top:214px;color:var(--white);font-family:"Lato",sans-serif;font-weight:700;font-size:14px}
.hero-title{left:204px;top:234px;color:var(--white);font-family:"Lato",sans-serif;font-weight:700;font-size:37px;line-height:40px}
.hero-rule{left:204px;top:318px;width:218px;height:2px;background:var(--white)}
.dots{left:50px;top:262px}
.dots i{display:block;width:10px;height:10px;border:1px solid var(--white);border-radius:50%;margin-bottom:9px}
.dots i.on{background:var(--white)}

/* side labels */
.side-label{font-family:"Lato",sans-serif;font-size:18px;color:var(--ink);transform:rotate(-90deg);transform-origin:left top;white-space:nowrap}
.side-line{width:1px;background:var(--green)}

/* services */
.service{position:absolute;width:180px;text-align:center;font-family:"Lato",sans-serif;font-weight:700;font-size:12px;color:var(--muted)}
.service .ring{width:82px;height:82px;border:3px solid #c9c9c9;border-radius:50%;margin:0 auto 22px;display:flex;align-items:center;justify-content:center}
.service svg{width:40px;height:40px;fill:none;stroke:#aaa;stroke-width:2.4;stroke-linecap:round;stroke-linejoin:round}
.service.active{color:var(--green)}
.service.active .ring{border-color:var(--green)}
.service.active svg{stroke:var(--green)}
.chev{color:#aaa;font-size:22px;font-family:"Lato",sans-serif}

.detail-kicker{left:197px;top:853px;font-family:"Lato",sans-serif;font-size:12px;color:var(--muted)}
.detail-title{left:197px;top:872px;font-family:"Lato",sans-serif;font-weight:700;font-size:27px;color:var(--green)}
.short-rule{height:2px;width:32px;background:var(--green)}
.detail-lead{left:197px;top:955px;width:420px;font-weight:700;font-size:12.5px;line-height:17px;color:var(--ink)}
.detail-body{left:197px;top:1001px;width:420px;font-size:11.5px;line-height:18px;color:var(--muted)}
.key-photo{left:590px;top:807px;width:470px;height:334px;background:radial-gradient(closest-side,#3a3a3a 0%,#7a7a7a 45%,rgba(255,255,255,0) 100%)}

/* works */
.works{left:0;top:1163px;width:1200px;height:649px;background:var(--light)}
.works-kicker{left:0;width:1200px;top:1243px;text-align:center;font-size:12px;color:var(--muted);font-family:"Lato",sans-serif}
.works-title{left:0;width:1200px;top:1260px;text-align:center;font-family:"Lato",sans-serif;font-weight:700;font-size:28px;color:var(--green)}
.tile{position:absolute;width:210px;height:139px}

/* best */
.best-photo{left:0;top:1812px;width:597px;height:481px;background:linear-gradient(135deg,#5d7a3a 0%,#8a8a80 40%,#b9b4aa 70%,#e6e6e6 100%)}
.best-panel{left:597px;top:1812px;width:603px;height:481px;background:var(--green)}
.best-title{left:697px;width:400px;top:1925px;text-align:center;font-family:"Lato",sans-serif;font-weight:700;font-size:38px;line-height:44px;color:var(--white);letter-spacing:.5px}
.best-rule{left:718px;top:2022px;width:362px;height:2px;background:var(--white)}
.best-body{left:700px;width:396px;top:2048px;text-align:center;font-size:12.5px;line-height:22px;color:var(--white)}

/* cta */
.cta-text{left:171px;top:2343px;font-family:"Lato",sans-serif;font-weight:900;font-size:18px;line-height:24px;color:var(--ink)}
.cta-text em{font-style:normal;color:var(--green)}
.cta-small{left:173px;top:2405px;font-size:11px;color:#666}

/* map */
.map{left:0;top:2464px;width:1200px;height:355px;background:linear-gradient(120deg,#e9ead9 0%,#dfe8cf 30%,#c7d8ee 45%,#e5e7dc 60%,#d9e6c6 80%,#ecebdd 100%)}

/* footer */
.footer{left:0;top:2819px;width:1200px;height:413px;background:var(--footer);color:#eee}
.footer-base{left:0;top:3232px;width:1200px;height:59px;background:var(--footer-base);color:#ccc;font-size:10.5px;display:flex;align-items:center;justify-content:center}
.footer-logo{left:171px;top:2886px;color:var(--white);font-family:"Lato",sans-serif;font-weight:900;font-size:19px;line-height:20px;text-transform:uppercase;display:flex;gap:10px;align-items:center}
.footer-logo i{width:14px;height:14px;background:var(--white);display:block}
.footer-about{left:171px;top:2953px;width:240px;font-size:11px;line-height:17px;color:#eee}
.footer-contact{left:171px;top:3027px;font-size:10.5px;line-height:22px;color:#eee}
.footer-contact div{display:flex;align-items:center;gap:8px}
.footer-contact svg{width:10px;height:10px;fill:#eee}
.social{left:171px;top:3122px;display:flex;gap:8px}
.social i{width:10px;height:10px;border-radius:50%;background:var(--green);display:block}
.footer-h{font-family:"Lato",sans-serif;font-weight:900;font-size:15px;color:var(--white)}
.post{position:absolute;left:476px;width:270px;display:flex;gap:14px}
.post .thumb{width:50px;height:50px;flex:none;background:linear-gradient(135deg,#cfd8dc,#8aa0b0)}
.post p{font-size:10.5px;line-height:15px;color:#ddd}
.field{position:absolute;left:781px;width:219px;background:var(--white);border-radius:3px;font-size:11px;color:#888;padding:9px 12px}
</style>
</head>
<body>

<!-- top bar -->
<div class="abs topbar">
  <span style="left:88px"><svg viewBox="0 0 10 10"><path d="M5 0a3.5 3.5 0 0 0-3.5 3.5C1.5 6 5 10 5 10s3.5-4 3.5-6.5A3.5 3.5 0 0 0 5 0zm0 5a1.5 1.5 0 1 1 0-3 1.5 1.5 0 0 1 0 3z"/></svg>48 Harlow St, Southbank, VIC 3006</span>
  <span style="left:344px"><svg viewBox="0 0 10 10"><path d="M2 0l2 2.5-1 1.2a6 6 0 0 0 3.3 3.3l1.2-1L10 8l-1.5 2C4 10 0 6 0 1.5z"/></svg>+00 000 000 0000</span>
  <span style="left:470px"><svg viewBox="0 0 10 10"><path d="M0 2h10v6H0zM0 2l5 3.5L10 2" stroke="#222" stroke-width=".8"/></svg>info@callowaylanelocksmiths.com</span>
</div>

<!-- hero -->
<div class="abs hero-panel"></div>
<div class="abs hero-photo" role="img" aria-label="Close-up photo of a car key with remote buttons inserted into an ignition"></div>
<div class="abs logo"><i></i><div>Calloway Lane<br>Locksmiths</div></div>
<nav class="abs nav">
  <a style="left:535px">HOME</a>
  <a style="left:614px">ABOUT US</a>
  <a style="left:724px">SERVICES</a>
  <a style="left:805px">CONTACT US</a>
  <span class="btn btn-green" style="left:917px;top:-6px;width:101px;height:31px">Get a quote</span>
</nav>
<div class="abs dots"><i></i><i class="on"></i><i></i></div>
<div class="abs hero-kicker">Sed ut perspiciatis</div>
<h1 class="abs hero-title">Car key<br>Replacement</h1>
<div class="abs hero-rule"></div>
<span class="btn btn-dark" style="left:202px;top:355px;width:116px;height:33px">Contact us</span>

<!-- services -->
<div class="abs side-line" style="left:57px;top:575px;height:40px"></div>
<div class="abs side-label" style="left:46px;top:732px">Services</div>
<div class="abs side-line" style="left:57px;top:748px;height:30px"></div>

<span class="abs chev" style="left:178px;top:680px">&#8249;</span>
<span class="abs chev" style="left:1008px;top:680px">&#8250;</span>

<div class="service active" style="left:178px;top:640px">
  <div class="ring"><svg viewBox="0 0 40 40"><rect x="9" y="17" width="22" height="17" rx="2"/><path d="M13 17v-5a7 7 0 0 1 14 0v5"/><path d="M20 24v4"/></svg></div>
  Immobiliser ECU Resetting
</div>
<div class="service" style="left:397px;top:640px">
  <div class="ring"><svg viewBox="0 0 40 40"><circle cx="13" cy="13" r="6"/><path d="M17 17l6 6M26 26l6 6M30 30l2-2M28 28l-2 2"/></svg></div>
  Broken Key Removal
</div>
<div class="service" style="left:616px;top:640px">
  <div class="ring"><svg viewBox="0 0 40 40"><rect x="13" y="10" width="14" height="24" rx="4"/><circle cx="20" cy="19" r="3"/><path d="M14 5a9 9 0 0 1 12 0"/></svg></div>
  Car Remote Controls
</div>
<div class="service" style="left:838px;top:640px">
  <div class="ring"><svg viewBox="0 0 40 40"><path d="M10 30V12h12l8 8v10z"/><path d="M22 12v8h8"/></svg></div>
  Car Opening
</div>

<div class="abs detail-kicker">Get a &nbsp;quote now!</div>
<h2 class="abs detail-title">Immobiliser ECU Resetting</h2>
<div class="abs short-rule" style="left:197px;top:932px"></div>
<p class="abs detail-lead">Sed ut perspiciatis unde omnis iste natus error sit voluptatem accusan tium doloremque</p>
<p class="abs detail-body">architecto beatae vitae dicta sunt explicabo. Nemo enim ipsam volu ptatem quia voluptas sit aspernatur aut odit aut fugit, sed quia con sequuntur magni dolores ...</p>
<div class="abs key-photo" role="img" aria-label="Photo of a black flip-out remote car key"></div>

<!-- recent works -->
<section class="abs works"></section>
<div class="abs side-line" style="left:57px;top:1163px;height:70px"></div>
<div class="abs side-label" style="left:46px;top:1365px">Recent works</div>
<div class="abs works-kicker">Ut enim ad minima veniam quis</div>
<h2 class="abs works-title">Works we have done recently</h2>
<div class="abs short-rule" style="left:584px;top:1322px"></div>

<div class="tile" style="left:169px;top:1367px;background:linear-gradient(135deg,#3d4448,#9aa3a8)" role="img" aria-label="Photo of hands unlocking a car door"></div>
<div class="tile" style="left:387px;top:1367px;background:linear-gradient(135deg,#555,#cfcfcf)" role="img" aria-label="Photo of a key in a frosted lock"></div>
<div class="tile" style="left:604px;top:1367px;background:linear-gradient(135deg,#5a5040,#a9a08c)" role="img" aria-label="Photo of a disassembled ignition barrel"></div>
<div class="tile" style="left:820px;top:1367px;background:linear-gradient(135deg,#2f3a44,#8896a2)" role="img" aria-label="Photo of a locksmith working inside a car door"></div>
<div class="tile" style="left:169px;top:1514px;background:linear-gradient(135deg,#2e4a66,#a6b6c4)" role="img" aria-label="Photo of a hand holding a car remote"></div>
<div class="tile" style="left:387px;top:1514px;background:linear-gradient(135deg,#222,#9a9a9a)" role="img" aria-label="Photo of a remote key pointed at a dark car"></div>
<div class="tile" style="left:604px;top:1514px;background:linear-gradient(135deg,#6a6a6a,#c9c6c0)" role="img" aria-label="Photo of a car key held beside a wheel"></div>
<div class="tile" style="left:820px;top:1514px;background:linear-gradient(135deg,#3e6e8c,#b7c9d3)" role="img" aria-label="Photo of keys hanging in a car door lock"></div>

<span class="btn btn-dark" style="left:542px;top:1714px;width:116px;height:35px">View all</span>

<!-- best locksmith -->
<div class="abs best-photo" role="img" aria-label="Photo of a locksmith opening a white car door"></div>
<div class="abs best-panel"></div>
<h2 class="abs best-title">BEST LOCKSMITH IN<br>MELBOURNE</h2>
<div class="abs best-rule"></div>
<p class="abs best-body">ed ut perspiciatis unde omnis iste natus error sit voluptatem accusantium doloremque laudantium, totam rem aperiam, eaque ipsa quae ab illo inventore veritatis et quasi architecto beatae vitae dicta sunt explicabo. Nemo enim ipsam voluptatem quia voluptas sit aspernatur aut odit aut fugit, sed quia consequuntur magni dolores eos qui ratione voluptatem sequi nesciunt. Neque porro quisquam est.</p>

<!-- call to action -->
<p class="abs cta-text">We are always there for your &nbsp;to take care of your car.<br>We offer <em>PROFESSIONAL ASSISTANCE</em>!</p>
<p class="abs cta-small">Ad minima veniam, quis nostrum exercitationem ullam corporis suscipit laboriosam.</p>
<span class="btn btn-dark" style="left:875px;top:2357px;width:115px;height:35px">Get a quote</span>

<!-- map -->
<div class="abs map" role="img" aria-label="Street map of the service area"></div>

<!-- footer -->
<footer class="abs footer"></footer>
<div class="abs footer-logo"><i></i><div>Calloway Lane<br>Locksmiths</div></div>
<p class="abs footer-about">Quis autem vel eum iure reprehenderit qui in ea voluptate velit esse quam nihil molestiae consequatur, vel illum qui dolorem eum fugiat</p>
<div class="abs footer-contact">
  <div><svg viewBox="0 0 10 10"><path d="M5 0a3.5 3.5 0 0 0-3.5 3.5C1.5 6 5 10 5 10s3.5-4 3.5-6.5A3.5 3.5 0 0 0 5 0z"/></svg>48 Harlow St, Southbank, VIC 3006</div>
  <div><svg viewBox="0 0 10 10"><path d="M2 0l2 2.5-1 1.2a6 6 0 0 0 3.3 3.3l1.2-1L10 8l-1.5 2C4 10 0 6 0 1.5z"/></svg>+00 000 000 0000</div>
  <div><svg viewBox="0 0 10 10"><path d="M0 2h10v6H0z"/></svg>info@callowaylanelocksmiths.com</div>
</div>
<div class="abs social"><i></i><i></i><i></i><i></i></div>

<h3 class="abs footer-h" style="left:476px;top:2897px">Recent Posts</h3>
<div class="post" style="top:2944px"><div class="thumb" role="img" aria-label="Blog post thumbnail photo"></div><p>Quis autem vel eum iure reprehenderit qui in ea voluptate velit esse quam nihil molestiae consequatur, vel illum</p></div>
<div class="post" style="top:3020px"><div class="thumb" role="img" aria-label="Blog post thumbnail photo"></div><p>Quis autem vel eum iure reprehenderit qui in ea voluptate velit esse quam nihil molestiae consequatur, vel illum</p></div>
<div class="post" style="top:3095px"><div class="thumb" role="img" aria-label="Blog post thumbnail photo"></div><p>Quis autem vel eum iure reprehenderit qui in ea voluptate velit esse quam nihil molestiae consequatur, vel illum</p></div>

<h3 class="abs footer-h" style="left:781px;top:2897px">Contact Form</h3>
<div class="field" style="top:2940px;height:33px">Name</div>
<div class="field" style="top:2984px;height:33px">E-mail</div>
<div class="field" style="top:3028px;height:69px">Messages</div>
<span class="btn btn-green" style="left:781px;top:3113px;width:114px;height:31px;font-size:10px">Send message</span>

<div class="abs footer-base">Calloway Lane Locksmiths © 2017 All Rights Reserved.</div>

</body>
</html>
```